Design Our Holiday Magic Coupon

Purpose - The purpose of this project is to create a festive, uplifting, and visually engaging physical coupon that will be mailed to our existing community and warm leads.
The intent is twofold: first, to spark delight and connection by offering a tangible, personal touch during the holiday season; and second, to encourage customers to explore and purchase our programs as they prepare for a strong start to 2026. This mailer is designed to re-engage past buyers, inspire current participants, and gently invite new momentum into their practice through a simple, friendly offer.

Project Description + Scope

This project includes the design and production of a printed coupon ( card format) featuring a 20% discount on purchases of $79 or more. The copy should feel warm, clear, and celebratory without urgency or pressure.

The front of the card will include the headline (“Live Your Best 2026”), bold discount information, and the coupon code FESTIVE20. The back will include a short message reinforcing the tone of possibility and ease, plus simple redemption instructions and the expiry date: December 31, 2025. Deliverables include print-ready artwork, color selection aligned with KH brand style.

one side
LIVE YOUR BEST 2026
Enjoy 20% OFF when you buy $79 or more.
Use code: FESTIVE20
Redeem until end of day December 31, 2025.

Back side - Move with clarity.
Heal with intelligence.
Lead with ease.
Thank you for being part of Kinetic Harmony.
Lots of love, Mara and the whole of Team Mara

Target Market(s)

yoga teachers, yoga lovers, mostly over 50 years, women

Font styles to use
Other font styles liked:
• see attached for feel

Colors
0054AA
0677BA
7BADD7
CADEEF
E8F1F8
0094D4
00A9DD
6FCCEA
C7EBF8
E9F6FB
00AB8E
00BBA5
67D7C9
C6EFE9
E9F9F6
EB3D1F
EC4F4E
F09395
F8D3D4
FCEDEE

Requirements
Nice to have
• see attached

```html
<!DOCTYPE html>
<html lang="en">
<head>
<meta charset="utf-8">
<title>Holiday Coupon – Kinetic Harmony</title>
<link rel="stylesheet" href="https://fonts.googleapis.com/css2?family=Roboto+Condensed:ital,wght@0,400;0,700;1,400&display=swap">
<style>
  :root {
    --page-bg: #e4e4e4;
    --card-bg: #ffffff;
    --ticket-orange: #f9b043;
    --ink: #111111;
    --stitch-light: #ffffff;
    --code-box: #ffffff;
  }
  * { margin: 0; padding: 0; box-sizing: border-box; }
  html, body {
    width: 1051px;
    height: 1200px;
    overflow: hidden;
    background: var(--page-bg);
    font-family: "Roboto Condensed", "Arial Narrow", sans-serif;
    color: var(--ink);
  }
  .coupon-card {
    position: absolute;
    left: 100px;
    width: 850px;
    height: 530px;
    background: var(--card-bg);
  }
  .coupon-card--front { top: 52px; }
  .coupon-card--back { top: 613px; }
  .coupon-card__art {
    position: absolute;
    inset: 0;
    width: 850px;
    height: 530px;
  }
  .ticket-shape { fill: var(--ticket-orange); }
  .cut-line {
    fill: none;
    stroke: var(--ink);
    stroke-width: 1.6;
    stroke-dasharray: 24 16;
  }
  .stitch-line {
    fill: none;
    stroke: var(--stitch-light);
    stroke-width: 1.3;
    stroke-dasharray: 18 14;
  }
  .coupon-text {
    position: absolute;
    left: 0;
    width: 850px;
    text-align: center;
    line-height: 1;
    white-space: nowrap;
  }
  .headline {
    font-weight: 700;
    font-size: 66px;
    letter-spacing: -0.5px;
  }
  .headline--front { top: 157px; }
  .headline--back { top: 129px; letter-spacing: -1px; }
  .offer-line { top: 246px; font-size: 22px; }
  .offer-line strong { font-weight: 700; }
  .code-badge {
    position: absolute;
    top: 291px;
    left: 311px;
    width: 228px;
    height: 38px;
    background: var(--code-box);
    font-weight: 700;
    font-size: 22px;
    line-height: 38px;
    text-align: center;
  }
  .expiry-line { top: 351px; font-size: 22px; font-style: italic; }
  .message-line { font-size: 21px; }
  .message-line--1 { top: 219px; }
  .message-line--2 { top: 272px; }
  .message-line--3 { top: 325px; }
  .message-line--4 { top: 376px; }
</style>
</head>
<body>

<section class="coupon-card coupon-card--front" aria-label="Coupon front">
  <svg class="coupon-card__art" viewBox="0 0 850 530" aria-hidden="true">
    <path class="cut-line" d="M 68 26 H 782 A 40 40 0 0 0 822 66 V 464 A 40 40 0 0 0 782 504 H 68 A 40 40 0 0 0 28 464 V 66 A 40 40 0 0 0 68 26 Z"/>
    <path class="ticket-shape" d="M 86 53 H 764 A 33 33 0 0 0 797 86 V 444 A 33 33 0 0 0 764 477 H 86 A 33 33 0 0 0 53 444 V 86 A 33 33 0 0 0 86 53 Z"/>
    <path class="stitch-line" d="M 112 78 H 733 L 768 113 V 416 L 733 451 H 112 L 77 416 V 113 Z"/>
  </svg>
  <h1 class="coupon-text headline headline--front">LIVE YOUR BEST 2026</h1>
  <p class="coupon-text offer-line">Enjoy <strong>20% OFF</strong> when you buy <strong>$79</strong> or more.</p>
  <p class="code-badge">Use code: FESTIVE20</p>
  <p class="coupon-text expiry-line">Redeem until end of day December 31, 2025.</p>
</section>

<section class="coupon-card coupon-card--back" aria-label="Coupon back">
  <svg class="coupon-card__art" viewBox="0 0 850 530" aria-hidden="true">
    <path class="cut-line" d="M 68 26 H 782 A 40 40 0 0 0 822 66 V 464 A 40 40 0 0 0 782 504 H 68 A 40 40 0 0 0 28 464 V 66 A 40 40 0 0 0 68 26 Z"/>
    <path class="ticket-shape" d="M 86 53 H 764 A 33 33 0 0 0 797 86 V 444 A 33 33 0 0 0 764 477 H 86 A 33 33 0 0 0 53 444 V 86 A 33 33 0 0 0 86 53 Z"/>
    <path class="stitch-line" d="M 112 78 H 733 L 768 113 V 416 L 733 451 H 112 L 77 416 V 113 Z"/>
  </svg>
  <h2 class="coupon-text headline headline--back">Move with clarity.</h2>
  <p class="coupon-text message-line message-line--1">Heal with intelligence.</p>
  <p class="coupon-text message-line message-line--2">Lead with ease.</p>
  <p class="coupon-text message-line message-line--3">Thank you for being part of Kinetic Harmony.</p>
  <p class="coupon-text message-line message-line--4">Lots of love, Mara and the whole of Team Mara</p>
</section>

</body>
</html>
```